Business Card & Stationary
for Dental office
Professional
Ritika Dhulekar, DDS
18467 E Larchmont Rd
Harlow Springs, MI 49907
toothclinic@mailbrook.com
PineLedgeDental.com
Logo has business name.
Back of business card will be used for pre-printed appointment information.
Business logo on Gray color
Business Logo
Sample back of card

```html
<!DOCTYPE html>
<html lang="en">
<head>
<meta charset="utf-8">
<title>Pine Ledge Dental – Stationery Concepts</title>
<link href="https://fonts.googleapis.com/css2?family=Open+Sans:wght@400;600;700&display=swap" rel="stylesheet">
<style>
  :root{
    --stage:#3b2f28;
    --paper:#ffffff;
    --blue-deep:#1f4fbf;
    --blue-mid:#3a7ae0;
    --blue-light:#5fb4ea;
    --ink:#4a5568;
    --ink-soft:#8a94a6;
    --label:#e9e2da;
    --flap-line:#c9ced6;
  }
  *{margin:0;padding:0;box-sizing:border-box}
  html,body{width:1200px;height:466px;overflow:hidden;background:var(--stage);font-family:"Open Sans",Arial,sans-serif}
  .canvas{position:relative;width:1200px;height:466px}
  .piece{position:absolute;background:var(--paper);overflow:hidden;box-shadow:0 2px 6px rgba(0,0,0,.35)}
  .piece svg.art{position:absolute;inset:0;width:100%;height:100%}
  .label{position:absolute;color:var(--label);font-size:6px;font-weight:600;letter-spacing:.12em;text-transform:uppercase;text-align:center}
  .logo{position:absolute;display:flex;align-items:center;gap:4px;color:var(--blue-deep);font-weight:700;letter-spacing:.06em;white-space:nowrap}
  .logo .mark{background:var(--blue-deep)}
  .text{position:absolute;color:var(--ink);line-height:1.45;white-space:nowrap}
  .rule{position:absolute;height:1px;background:var(--ink-soft)}
</style>
</head>
<body>
<div class="canvas">

  <div class="label" style="left:6px;top:270px;width:150px;text-align:left">Stationery Concepts</div>

  <div class="piece card-front" style="left:12px;top:283px;width:138px;height:72px">
    <svg class="art" viewBox="0 0 138 72" preserveAspectRatio="none">
      <path d="M138,40 C118,58 96,68 70,72 L138,72 Z" fill="var(--blue-light)"/>
      <path d="M138,52 C122,64 108,70 92,72 L138,72 Z" fill="var(--blue-deep)"/>
    </svg>
    <div class="logo" style="left:8px;top:8px;font-size:5.5px"><span class="mark" style="width:6px;height:6px"></span>PINE LEDGE DENTAL</div>
    <div class="text" style="left:8px;top:24px;font-size:4.2px">
      <strong>Ritika Dhulekar, DDS</strong><br>
      18467 E Larchmont Rd<br>
      Harlow Springs, MI 49907<br>
      Tel 734-555-0142<br>
      toothclinic@mailbrook.com<br>
      PineLedgeDental.com
    </div>
  </div>
  <div class="label" style="left:12px;top:361px;width:138px">Business Card Front</div>

  <div class="piece card-back" style="left:12px;top:375px;width:138px;height:72px">
    <div class="text" style="left:8px;top:7px;font-size:4.5px;font-weight:600">Your next appointment is</div>
    <div class="text" style="left:8px;top:20px;font-size:4px">Date</div>
    <div class="rule" style="left:22px;top:25px;width:100px"></div>
    <div class="text" style="left:8px;top:32px;font-size:4px">Time</div>
    <div class="rule" style="left:22px;top:37px;width:100px"></div>
    <div class="rule" style="left:8px;top:49px;width:114px"></div>
    <div class="text" style="left:8px;top:56px;font-size:3.6px;color:var(--ink-soft)">Please call 24 hours ahead to reschedule.</div>
  </div>
  <div class="label" style="left:12px;top:452px;width:138px">Business Card Back</div>

  <div class="piece letterhead-one" style="left:192px;top:36px;width:257px;height:401px">
    <svg class="art" viewBox="0 0 257 401" preserveAspectRatio="none">
      <path d="M257,0 L224,0 C196,120 196,270 236,401 L257,401 Z" fill="var(--blue-light)"/>
      <path d="M257,0 L236,0 C214,120 214,270 246,401 L257,401 Z" fill="var(--blue-deep)"/>
      <path d="M222,0 C192,120 192,270 232,401" fill="none" stroke="var(--blue-mid)" stroke-width="1"/>
    </svg>
    <div class="logo" style="left:50%;top:14px;transform:translateX(-50%);font-size:7px"><span class="mark" style="width:7px;height:7px"></span>PINE LEDGE DENTAL</div>
    <div class="text" style="left:105px;bottom:10px;transform:translateX(-50%);font-size:3.6px;color:var(--ink-soft)">18467 E Larchmont Rd · Harlow Springs, MI 49907 · toothclinic@mailbrook.com · PineLedgeDental.com</div>
  </div>
  <div class="label" style="left:192px;top:442px;width:257px">Letter Head Option 1</div>

  <div class="piece letterhead-two" style="left:475px;top:36px;width:257px;height:401px">
    <svg class="art" viewBox="0 0 257 401" preserveAspectRatio="none">
      <path d="M0,352 C70,392 170,372 257,300 L257,401 L0,401 Z" fill="var(--blue-light)"/>
      <path d="M0,372 C80,404 180,384 257,330 L257,401 L0,401 Z" fill="var(--blue-deep)"/>
      <path d="M0,346 C70,386 170,366 257,294" fill="none" stroke="var(--blue-mid)" stroke-width="1"/>
    </svg>
    <div class="logo" style="left:50%;top:14px;transform:translateX(-50%);font-size:7px"><span class="mark" style="width:7px;height:7px"></span>PINE LEDGE DENTAL</div>
    <div class="text" style="left:50%;top:326px;transform:translateX(-50%);font-size:3.6px;color:var(--ink-soft)">18467 E Larchmont Rd · Harlow Springs, MI 49907 · PineLedgeDental.com</div>
  </div>
  <div class="label" style="left:475px;top:442px;width:257px">Letter Head Option 2</div>

  <div class="piece envelope-back" style="left:768px;top:36px;width:408px;height:104px;background:var(--blue-deep)">
    <svg class="art" viewBox="0 0 408 104" preserveAspectRatio="none">
      <path d="M0,0 L408,0 L408,30 C300,42 110,42 0,30 Z" fill="var(--blue-light)"/>
      <path d="M0,104 C120,70 290,70 408,104" fill="none" stroke="var(--blue-mid)" stroke-width="1.5"/>
    </svg>
  </div>

  <div class="piece envelope-white" style="left:768px;top:190px;width:408px;height:104px">
    <svg class="art" viewBox="0 0 408 104" preserveAspectRatio="none">
      <path d="M2,2 L406,2 L406,34 C300,46 110,46 2,34 Z" fill="none" stroke="var(--flap-line)" stroke-width="1"/>
    </svg>
  </div>

  <div class="piece envelope-front" style="left:768px;top:326px;width:408px;height:106px">
    <svg class="art" viewBox="0 0 408 106" preserveAspectRatio="none">
      <path d="M408,0 L360,0 C330,40 340,80 372,106 L408,106 Z" fill="var(--blue-light)"/>
      <path d="M408,0 L378,0 C352,40 360,80 388,106 L408,106 Z" fill="var(--blue-deep)"/>
    </svg>
    <div class="logo" style="left:12px;top:10px;font-size:6px"><span class="mark" style="width:6px;height:6px"></span>PINE LEDGE DENTAL</div>
    <div class="text" style="left:12px;top:22px;font-size:3.8px;color:var(--ink-soft)">18467 E Larchmont Rd<br>Harlow Springs, MI 49907</div>
  </div>
  <div class="label" style="left:768px;top:442px;width:408px">Envelope Options</div>

</div>
</body>
</html>
```